Refresh Velcor Web Presence - www.velcor-example.com

Velcor (www.velcor-example.com)web site needs a makeover. It needs to be more modern, less cluttered, more corporate, prestigious, user friendly, impressive, up to date. We want a modern corporate image that encourages our business users to trust us and buy our products and services. They need to understand that they are dealing with a highly reputable, long established company, but one that is up to date and forward thinking.
1. Clean uncluttered design.
2. Domain Registration box and Countries (price) box to be collapsible and expandable.
3. All links on page need to be conserved for SEO but hidden from view.
4. Logo and general colour scheme need to be retained.
5. Phone number to be prominently displayed at top of page.
6. No calls to action (CTA) below the fold.
7. Sites we like: www.plinvaro-example.com, www.dunmerry-example.com,www.zup.example,www.tavisk-example.com, www.fembly-example.com (busy but clear CTAs), www.lumtrek-example.com
Updates
Project Deadline Extended
Reason: We lost a lot of time to review over the holiday weekend. We need to have a chance to interact during business hours.
Target Market(s)
Small business to large enterprise
Industry/Entity Type
Business
Look and feel

```html
<!DOCTYPE html>
<html lang="en">
<head>
<meta charset="utf-8">
<title>Velcor — Domain Registration</title>
<link href="https://fonts.googleapis.com/css2?family=Arimo:wght@400;700&display=swap" rel="stylesheet">
<style>
:root{
  --navy:#2a3590;
  --orange:#f39321;
  --orange-light:#f8ac36;
  --orange-dark:#e6781a;
  --text:#333;
  --line:#e3e3e3;
  --panel:#eef0f4;
  --card:#e9e9e9;
  --btn:#5a5a5a;
}
*{box-sizing:border-box;margin:0;padding:0}
html,body{width:842px;height:1200px;overflow:hidden;background:#fff}
body{font-family:"Arimo",Arial,sans-serif;color:var(--text)}
.page{width:1018px;height:1450px;position:relative;transform:scale(.8271);transform-origin:0 0}
.abs{position:absolute}

/* top bar */
.topbar{left:0;top:0;width:1018px;height:42px;background:var(--navy)}
.topnav{left:100px;top:0;height:42px;display:flex}
.topnav a{color:#fff;font-size:13px;text-decoration:none;line-height:42px;padding:0 16px;border-right:1px solid rgba(255,255,255,.18)}
.topnav a.current{background:#fff;color:var(--text);padding:0 17px}
.whois{left:543px;top:8px;width:122px;height:25px;background:#fff;border-radius:4px;font-size:10px;font-style:italic;color:#aaa;line-height:25px;padding-left:10px}
.whois svg{position:absolute;right:8px;top:7px}
.cart{left:693px;top:0;line-height:42px;color:#fff;font-size:13px}
.cart b{display:inline-block;width:15px;height:15px;border-radius:50%;background:var(--orange);font-size:10px;line-height:15px;text-align:center;margin-left:4px}
.callus{left:767px;top:7px;color:#fff;font-size:20px;font-weight:700;display:flex;gap:10px;align-items:center}

/* header */
.logo{left:92px;top:88px;display:flex;align-items:center;gap:12px}
.logo i{width:22px;height:22px;border-radius:50%;background:var(--orange);display:block}
.logo span{font-size:46px;font-weight:700;color:var(--navy);letter-spacing:1px}
.brace{left:326px;top:52px;font-size:96px;color:var(--navy);font-weight:400}
.globe{left:378px;top:62px;width:112px;height:112px;border-radius:50%;background:radial-gradient(circle at 38% 35%,#8cc4ee,#2a74c4 60%,#15457f)}
.headline{left:521px;top:68px;font-size:29px;font-weight:700;color:#3a3a3a}
.headline em{font-style:normal;color:var(--orange)}
.subline{left:521px;top:101px;font-size:19px;color:#a5a5a5}

/* main nav */
.mainnav{left:0;top:193px;width:1018px;height:47px;background:linear-gradient(#f9ad37,#f08b1d)}
.mainnav ul{position:absolute;left:88px;top:0;display:flex;list-style:none}
.mainnav li{color:#fff;font-weight:700;font-size:16px;line-height:47px;padding:0 15px;border-right:1px solid rgba(255,255,255,.35)}
.mainnav li:last-child{border:0}

/* section heads */
.shead{display:flex;align-items:center;gap:10px}
.shead .ic{width:36px;height:36px;border-radius:50%;background:var(--orange);display:flex;align-items:center;justify-content:center}
.shead h2{font-size:20px;font-weight:700;color:#333}
.shead .hide{background:#e6e6e6;font-size:12px;font-weight:700;color:#555;padding:6px 9px;margin-left:6px}
.rule{height:1px;background:var(--line)}

/* search */
.search{left:115px;top:331px;width:414px;height:42px;border:2px solid #ddd;font-size:18px;font-weight:700;line-height:38px;padding-left:12px;color:#333}
.searchbtn{left:538px;top:331px;width:101px;height:42px;background:linear-gradient(var(--orange-light),var(--orange-dark));color:#fff;font-weight:700;font-size:15px;text-align:center;line-height:42px}
.tabs{left:115px;top:386px;width:524px;display:flex;justify-content:space-between;font-size:13.5px;color:#444;white-space:nowrap}
.tabs .on{color:var(--orange)}
.regions{left:115px;top:412px;width:524px;height:37px;background:var(--orange);display:flex;color:#fff;font-size:13.5px}
.regions span{line-height:37px;flex:1;text-align:center;white-space:nowrap}
.regions .on{background:var(--orange-dark);flex:0 0 102px}

.group{left:117px;width:524px}
.group h3{font-size:13px;font-weight:700;color:#555;margin-bottom:6px}
.grid{display:grid;grid-template-columns:repeat(6,85px);row-gap:8px;font-size:12px;color:#555}
.grid span{display:flex;align-items:center;gap:5px;height:14px;white-space:nowrap}
.grid span::before{content:"";width:11px;height:11px;border:1px solid #bbb;border-radius:2px;background:#fafafa;flex:none}
.grid span.chk{position:relative}
.grid span.chk::before{border-color:#555;background:#fff}
.grid span.chk svg{position:absolute;left:0;top:-1px}

/* countries */
.ctable{left:659px;top:332px;width:241px;border-collapse:collapse;font-size:12px}
.ctable th{background:#eaeaea;font-weight:700;text-align:left;height:26px;padding:0 6px;font-size:12px;line-height:12px}
.ctable th.p{text-align:center}
.ctable td{height:21px;padding:0 6px;border-bottom:1px solid #fff}
.ctable td.n{color:#777;background:#f4f4f4}
.ctable td.p{text-align:right;padding-right:0}
.ctable td.t{white-space:nowrap;padding-left:8px}
.flag{display:inline-block;width:13px;height:9px;vertical-align:-1px;margin-right:3px}
.fullist{left:660px;top:748px;font-size:12px;font-weight:700;color:#444}

.paybox{left:659px;top:808px;width:241px;height:207px;background:var(--panel);text-align:center}
.paybox .star{position:absolute;left:97px;top:-18px;width:38px;height:38px;border-radius:50%;background:var(--orange);display:flex;align-items:center;justify-content:center;border:2px solid #fff}
.paybox h4{font-size:12px;font-weight:700;margin-top:30px;color:#333}
.paybox p{font-size:10px;color:#555}
.cards{display:flex;gap:3px;justify-content:center;margin:14px 0 6px}
.cards i{width:44px;height:24px;background:#fff;border:1px solid #cfd3db;border-radius:2px}
.powered{text-align:left;padding-left:27px;font-size:8px;color:var(--navy);font-weight:700}
.powered b{display:block;font-size:19px;font-weight:400;color:var(--navy);line-height:20px}

/* learn more */
.learn{left:116px;top:1040px;width:784px;display:flex;align-items:center;gap:14px;font-size:20px;font-weight:700;color:#444}
.learn::before,.learn::after{content:"";flex:1;height:1px;background:var(--line)}
.card{top:1084px;width:241px;height:326px;background:var(--card);text-align:center}
.card .ph{height:151px}
.card .ic{position:absolute;left:102px;top:133px;width:36px;height:36px;border-radius:50%;background:var(--orange);border:2px solid #fff;display:flex;align-items:center;justify-content:center}
.card h5{font-size:12px;font-weight:700;margin-top:30px;color:#222}
.card p{font-size:10px;line-height:17px;color:#444;margin:10px 12px 0}
.card .btn{display:inline-block;background:var(--btn);color:#fff;font-size:10px;font-weight:700;padding:7px 9px;margin-top:13px}
.footer{left:0;top:1437px;width:1018px;height:13px;background:#e5e5e5}
</style>
</head>
<body>
<div class="page">

  <div class="abs topbar"></div>
  <nav class="abs topnav">
    <a class="current">Home</a><a>Register</a><a>Log In</a><a>FAQ</a><a>Support</a><a>Contact</a>
  </nav>
  <div class="abs whois">Whois SEARCH<svg width="7" height="11" viewBox="0 0 7 11"><path d="M1 1l4.5 4.5L1 10" stroke="#aaa" fill="none" stroke-width="1.5"/></svg></div>
  <div class="abs cart">Cart<b>2</b></div>
  <div class="abs callus">
    <svg width="26" height="26" viewBox="0 0 24 24"><path fill="#fff" d="M6.6 10.8a15.1 15.1 0 0 0 6.6 6.6l2.2-2.2a1 1 0 0 1 1-.25 11.4 11.4 0 0 0 3.6.57 1 1 0 0 1 1 1V20a1 1 0 0 1-1 1A17 17 0 0 1 3 4a1 1 0 0 1 1-1h3.5a1 1 0 0 1 1 1c0 1.25.2 2.45.57 3.57a1 1 0 0 1-.25 1z"/></svg>
    Call us!
  </div>

  <div class="abs logo"><i></i><span>Velcor</span></div>
  <div class="abs brace">{</div>
  <div class="abs globe" role="img" aria-label="Globe showing the world's continents"></div>
  <div class="abs headline"><em>300+</em> domain name extensions</div>
  <div class="abs subline">Accredited in over 100 countries</div>

  <div class="abs mainnav"><ul>
    <li>Domain names</li><li>IDN domains</li><li>New gTLDs</li><li>Phone Numbers</li><li>Hosting</li><li>Resellers</li><li>About us</li>
  </ul></div>

  <div class="abs shead" style="left:115px;top:262px">
    <span class="ic"><svg width="20" height="16" viewBox="0 0 20 16"><path fill="#fff" d="M5 15a4 4 0 0 1-.6-8A6 6 0 0 1 16 6a4.5 4.5 0 0 1-1 9z"/></svg></span>
    <h2>DOMAIN REGISTRATION</h2><span class="hide">HIDE</span>
  </div>
  <div class="abs rule" style="left:115px;top:316px;width:524px"></div>
  <div class="abs search">www.yourdomain.com</div>
  <div class="abs searchbtn">SEARCH!</div>
  <div class="abs tabs"><span class="on">Domain Registration</span><span>IDN</span><span>Bulk Search</span><span>Transfer</span><span>Renew</span><span>Map Search</span><span>PhNUM</span></div>
  <div class="abs regions"><span class="on">Popular</span><span>Europe</span><span>Asia/Pacific</span><span>America</span><span>Africa</span><span>Generic</span></div>

  <div class="abs group" style="top:461px"><h3>Generic Domains</h3><div class="grid">
    <span class="chk"><svg width="13" height="13" viewBox="0 0 13 13"><path d="M2 6.5l3 3L12 1" stroke="#2a3590" stroke-width="2" fill="none"/></svg>.co</span>
    <span class="chk"><svg width="13" height="13" viewBox="0 0 13 13"><path d="M2 6.5l3 3L12 1" stroke="#2a3590" stroke-width="2" fill="none"/></svg>.com</span>
    <span>.info</span><span>.me</span><span>.mobi</span><span>.name</span>
    <span>.net</span><span>.org</span><span>.xxx</span>
  </div></div>

  <div class="abs group" style="top:540px"><h3>Europe Domains</h3><div class="grid">
    <span>.at</span><span>.be</span><span>.eu</span><span>.eu.com</span><span>.fr</span><span>.de</span>
    <span>.de.com</span><span>.gr.com</span><span>.ie</span><span>.im</span><span>.co.il</span><span>.it</span>
    <span>.lv</span><span>.lu</span><span>.com.mt</span><span>.co.nl</span><span>.nl</span><span>.no</span>
    <span>.no.com</span><span>.pl</span><span>.com.pt</span><span>.pt</span><span>.ru</span><span>.ru.com</span>
    <span>.com.es</span><span>.es</span><span>.se</span><span>.com.tr</span><span>.com.ua</span><span>.co.uk</span>
    <span>.gb.com</span><span>.uk.com</span>
  </div></div>

  <div class="abs group" style="top:707px"><h3>Asia/Pacific Domains</h3><div class="grid">
    <span>.asia</span><span>.com.au</span><span>.cn</span><span>.cn.com</span><span>.com.hk</span><span>.hk</span>
    <span>.co.in</span><span>.in</span><span>.co.id</span><span>.my.id</span><span>.co.jp</span><span>.jp</span>
    <span>.com.my</span><span>.my</span><span>.co.nz</span><span>.com.sg</span><span>.sg</span><span>.co.kr</span>
    <span>.kr</span><span>.kr.com</span><span>.com.tw</span><span>.tw</span><span>.co.th</span><span>.ae</span>
    <span>.vn</span>
  </div></div>

  <div class="abs group" style="top:852px"><h3>America Domains</h3><div class="grid">
    <span>.ar.com</span><span>.com.ar</span><span>.br.com</span><span>.com.br</span><span>.ca</span><span>.cl</span>
    <span>.com.co</span><span>.dm</span><span>.com.do</span><span>.com.ec</span><span>.ec</span><span>.com.mx</span>
    <span>.mx</span><span>.com.pe</span><span>.pe</span><span>.com.pr</span><span>.sx</span><span>.north.am</span>
    <span>.south.am</span><span>.us</span><span>.us.com</span><span>.us.org</span>
  </div></div>

  <div class="abs group" style="top:975px"><h3>Africa Domains</h3><div class="grid">
    <span>.com.cm</span><span>.ly</span><span>.mw</span><span>.co.za</span><span>.cd</span><span>.co.ug</span>
  </div></div>

  <div class="abs shead" style="left:659px;top:262px">
    <span class="ic"><svg width="18" height="16" viewBox="0 0 18 16"><path fill="#fff" d="M1 2l5-1.5 6 2 5-1.5v13l-5 1.5-6-2-5 1.5z"/></svg></span>
    <h2>COUNTRIES</h2><span class="hide">HIDE</span>
  </div>
  <div class="abs rule" style="left:659px;top:316px;width:241px"></div>
  <table class="abs ctable">
    <tr><th>TLD</th><th>Country</th><th class="p">Price<br>(USD)</th></tr>
    <tr><td class="t"><i class="flag" style="background:linear-gradient(#d90012 33%,#0033a0 33% 66%,#f2a800 66%)"></i>.am</td><td class="n">Armenia</td><td class="p">$125.00</td></tr>
    <tr><td class="t"><i class="flag" style="background:linear-gradient(#e3262d 33%,#fff 33% 66%,#e3262d 66%)"></i>.at</td><td class="n">Austria</td><td class="p">$105.00</td></tr>
    <tr><td class="t"><i class="flag" style="background:linear-gradient(#c8313e 66%,#4aa657 66%)"></i>.by</td><td class="n">Belarus</td><td class="p">$185.00</td></tr>
    <tr><td class="t"><i class="flag" style="background:linear-gradient(90deg,#000 33%,#fdda24 33% 66%,#ef3340 66%)"></i>.be</td><td class="n">Belgium</td><td class="p">$105.00</td></tr>
    <tr><td class="t"><i class="flag" style="background:linear-gradient(#fff 50%,#d7141a 50%)"></i>.cz</td><td class="n">Czech Republic</td><td class="p">$105.00</td></tr>
    <tr><td class="t"><i class="flag" style="background:linear-gradient(90deg,#c8102e 30%,#fff 30% 44%,#c8102e 44%)"></i>.dk</td><td class="n">Denmark</td><td class="p">$105.00</td></tr>
    <tr><td class="t"><i class="flag" style="background:linear-gradient(#0072ce 33%,#000 33% 66%,#fff 66%)"></i>.ee</td><td class="n">Estonia</td><td class="p">$105.00</td></tr>
    <tr><td class="t"><i class="flag" style="background:#003399"></i>.eu</td><td class="n">European Union</td><td class="p">$56.00</td></tr>
    <tr><td class="t"><i class="flag" style="background:linear-gradient(90deg,#fff 28%,#003580 28% 46%,#fff 46%)"></i>.fi</td><td class="n">Finland</td><td class="p">$76.00</td></tr>
    <tr><td class="t"><i class="flag" style="background:linear-gradient(90deg,#0055a4 33%,#fff 33% 66%,#ef4135 66%)"></i>.fr</td><td class="n">France</td><td class="p">$105.00</td></tr>
    <tr><td class="t"><i class="flag" style="background:linear-gradient(#000 33%,#dd0000 33% 66%,#ffce00 66%)"></i>.de</td><td class="n">Germany</td><td class="p">$56.00</td></tr>
    <tr><td class="t"><i class="flag" style="background:repeating-linear-gradient(#0d5eaf 0 1px,#fff 1px 2px)"></i>.gr</td><td class="n">Greece</td><td class="p">$48.00</td></tr>
    <tr><td class="t"><i class="flag" style="background:linear-gradient(#fff 50%,#c8102e 50%)"></i>.gl</td><td class="n">Greenland</td><td class="p">$95.00</td></tr>
    <tr><td class="t"><i class="flag" style="background:linear-gradient(#cd2a3e 33%,#fff 33% 66%,#436f4d 66%)"></i>.hu</td><td class="n">Hungary</td><td class="p">$105.00</td></tr>
    <tr><td class="t"><i class="flag" style="background:linear-gradient(#0072ce 33%,#000 33% 66%,#fff 66%)"></i>.ee</td><td class="n">Estonia</td><td class="p">$105.00</td></tr>
    <tr><td class="t"><i class="flag" style="background:#003399"></i>.eu</td><td class="n">European Union</td><td class="p">$56.00</td></tr>
    <tr><td class="t"><i class="flag" style="background:linear-gradient(90deg,#fff 28%,#003580 28% 46%,#fff 46%)"></i>.fi</td><td class="n">Finland</td><td class="p">$76.00</td></tr>
    <tr><td class="t"><i class="flag" style="background:linear-gradient(90deg,#0055a4 33%,#fff 33% 66%,#ef4135 66%)"></i>.fr</td><td class="n">France</td><td class="p">$105.00</td></tr>
  </table>
  <div class="abs fullist">SEE FULL LIST</div>

  <div class="abs paybox">
    <span class="star"><svg width="18" height="18" viewBox="0 0 24 24"><path fill="#fff" d="M12 2l3 6.9 7.5.6-5.7 4.9 1.8 7.3L12 17.8 5.4 21.7l1.8-7.3L1.5 9.5 9 8.9z"/></svg></span>
    <h4>PAYMENT METHODS</h4>
    <p style="margin-top:12px">We accept the following payment methods:</p>
    <div class="cards"><i></i><i></i><i></i><i></i></div>
    <div class="powered">payments powered by<b>Paydrift</b></div>
    <p style="margin-top:14px;line-height:17px">You will receive an email invoice<br>for every order</p>
  </div>

  <div class="abs learn">LEARN MORE</div>

  <div class="abs card" style="left:116px">
    <div class="ph" role="img" aria-label="Photo of a woman working on a laptop at home" style="background:linear-gradient(135deg,#f4f1ec,#d8cfc2)"></div>
    <span class="ic"><svg width="18" height="18" viewBox="0 0 24 24"><circle cx="12" cy="8" r="4.5" fill="#fff"/><path fill="#fff" d="M3 22a9 9 0 0 1 18 0z"/></svg></span>
    <h5>YOUR OWN DOMAIN</h5>
    <p>Lorem Ipsum is simply dummy text of the printing and typesetting industry. Lorem Ipsum has been the industry's standard dummy text ever since the 1500s, when an unknown</p>
    <span class="btn">FIND OUT MORE</span>
  </div>
  <div class="abs card" style="left:387px">
    <div class="ph" role="img" aria-label="Photo of server racks in a data centre" style="background:linear-gradient(135deg,#2a2d33,#5b616b)"></div>
    <span class="ic"><svg width="20" height="16" viewBox="0 0 20 16"><path fill="#fff" d="M5 15a4 4 0 0 1-.6-8A6 6 0 0 1 16 6a4.5 4.5 0 0 1-1 9z"/></svg></span>
    <h5>NEW gTLDs</h5>
    <p>Lorem Ipsum is simply dummy text of the printing and typesetting industry. Lorem Ipsum has been the industry's standard dummy text ever since the 1500s, when an unknown</p>
    <span class="btn">FIND OUT MORE</span>
  </div>
  <div class="abs card" style="left:659px">
    <div class="ph" role="img" aria-label="Photo of business colleagues at an office desk" style="background:linear-gradient(135deg,#dfe3e6,#8a939c)"></div>
    <span class="ic"><svg width="22" height="16" viewBox="0 0 26 18"><circle cx="13" cy="5" r="4" fill="#fff"/><circle cx="5" cy="7" r="3" fill="#fff"/><circle cx="21" cy="7" r="3" fill="#fff"/><path fill="#fff" d="M5 18a8 8 0 0 1 16 0zM0 17a5 5 0 0 1 6-5l-2 5zM26 17a5 5 0 0 0-6-5l2 5z"/></svg></span>
    <h5>CORPORATE SERVICES</h5>
    <p>Lorem Ipsum is simply dummy text of the printing and typesetting industry. Lorem Ipsum has been the industry's standard dummy text ever since the 1500s, when an unknown</p>
    <span class="btn">FIND OUT MORE</span>
  </div>

  <div class="abs footer"></div>
</div>
</body>
</html>
```